Company or website name
- Marla Quade Design & Decor
- Links to the website
- Passionate about wedding floral design and decor. Events I create are timeless, classic and elegant, customized 100% to the brides’ desires. Inspiring them with a vision of what is possible & asking them to step inside it and see it for themselves
- Other Facts

```html
<!DOCTYPE html>
<html lang="en">
<head>
<meta charset="utf-8">
<title>Marla Quade Design &amp; Decor — Stationery</title>
<link href="https://fonts.googleapis.com/css2?family=Cormorant+Garamond:wght@400;500&family=Tinos&display=swap" rel="stylesheet">
<style>
  :root {
    --paper: #ffffff;
    --backdrop: #f7f5f6;
    --blush: #e8c2cf;
    --blush-light: #f1d7e0;
    --blush-deep: #d9a9ba;
    --ink: #4a4a4a;
    --white: #ffffff;
    --shadow: rgba(0, 0, 0, 0.12);
  }
  * { box-sizing: border-box; margin: 0; padding: 0; }
  html, body {
    width: 848px; height: 1200px; overflow: hidden;
    background: var(--backdrop);
  }
  .stationery-set { position: relative; width: 848px; height: 1200px; }

  .piece { position: absolute; box-shadow: 0 3px 10px var(--shadow); }

  /* Letterhead */
  .letterhead {
    left: 40px; top: 240px; width: 480px; height: 679px;
    background: var(--paper);
  }
  .letterhead__address {
    position: absolute; left: 300px; top: 40px;
    font: 10px/1.45 "Tinos", serif; color: var(--ink);
  }
  .letterhead__email {
    position: absolute; left: 300px; top: 140px;
    font: 10px "Tinos", serif; color: var(--ink);
  }
  .letterhead__band {
    position: absolute; left: 0; right: 0; bottom: 30px; height: 56px;
    background: var(--blush);
    display: flex; align-items: center; padding: 0 26px; gap: 18px;
  }
  .letterhead__web {
    position: absolute; left: 26px; bottom: 10px;
    font: 11px "Cormorant Garamond", serif; letter-spacing: 1px; color: var(--blush-deep);
  }

  /* Name block shared */
  .brand-name {
    font-family: "Cormorant Garamond", serif; font-weight: 500; color: var(--white);
    text-align: center; line-height: 1.15;
  }
  .ornament { background: linear-gradient(135deg, var(--white), var(--blush-light)); border-radius: 40%; opacity: 0.85; }

  /* Sticker label */
  .label-sticker {
    left: 560px; top: 240px; width: 250px; height: 110px;
    background: var(--paper); display: flex; align-items: center; justify-content: center;
  }
  .label-sticker__plate {
    background: var(--blush); padding: 14px 22px; border-radius: 10px;
  }

  /* Business card front */
  .card-front {
    left: 560px; top: 390px; width: 250px; height: 150px;
    background: var(--blush);
  }
  .card-front__stripe {
    position: absolute; left: 0; right: 0; top: 52px; height: 46px;
    border-top: 1px solid var(--white); border-bottom: 1px solid var(--white);
  }
  .card-front .brand-name {
    position: absolute; left: 28px; top: 52px; width: 150px; height: 46px;
    display: flex; flex-direction: column; justify-content: center; font-size: 15px;
  }

  /* Business card back */
  .card-back {
    left: 560px; top: 580px; width: 250px; height: 150px;
    background: var(--blush);
  }
  .card-back__contact {
    position: absolute; left: 16px; top: 18px;
    font: 7px/1.5 "Tinos", serif; color: var(--white);
  }
  .card-back__wordmark {
    position: absolute; left: 0; right: 0; top: 62px; text-align: center;
    font: 500 20px "Cormorant Garamond", serif; letter-spacing: 4px; color: var(--white);
  }
  .card-back__tagline {
    position: absolute; left: 0; right: 0; top: 90px; text-align: center;
    font: 500 9px "Cormorant Garamond", serif; letter-spacing: 3px; color: var(--white);
  }
  .card-back__rule {
    position: absolute; left: 16px; right: 16px; bottom: 22px; height: 1px; background: var(--white);
  }
</style>
</head>
<body>
<main class="stationery-set">

  <section class="piece letterhead">
    <address class="letterhead__address">
      Marla Quade<br>12 Willow Lane<br>Fairhaven<br>FH2 4QL<br>Tel: 0155-204-318<br>Fax: 0155-204-319
    </address>
    <p class="letterhead__email">hello@marlaquade.com</p>
    <div class="letterhead__band">
      <div class="ornament" role="img" aria-label="White floral swirl ornament" style="width:44px;height:30px;"></div>
      <p class="brand-name" style="font-size:14px;">Marla Quade<br>Design &amp; Decor</p>
      <div class="ornament" role="img" aria-label="White floral swirl ornament" style="width:44px;height:30px;"></div>
    </div>
    <p class="letterhead__web">www.marlaquade.com</p>
  </section>

  <section class="piece label-sticker">
    <div class="label-sticker__plate">
      <p class="brand-name" style="font-size:17px;">Marla Quade<br><span style="font-size:12px;">Design &amp; Decor</span></p>
    </div>
  </section>

  <section class="piece card-front">
    <div class="card-front__stripe"></div>
    <p class="brand-name">Marla Quade<span style="font-size:11px;">Design &amp; Decor</span></p>
    <div class="ornament" role="img" aria-label="White floral swirl ornament" style="position:absolute;left:182px;top:48px;width:52px;height:54px;"></div>
  </section>

  <section class="piece card-back">
    <p class="card-back__contact">12 Willow Lane<br>Fairhaven FH2 4QL<br>Tel 0155 204 318<br>hello@marlaquade.com</p>
    <p class="card-back__wordmark">MARLA QUADE</p>
    <p class="card-back__tagline">DESIGN &amp; DECOR</p>
    <div class="card-back__rule"></div>
  </section>

</main>
</body>
</html>
```